Marlene's 75th birthday

I need an invitation design for my aunt's 75th birthday party. The event will be created around the theme "Coming Home," and will also serve as a family reunion. We will be using an image of a salmon that she recently had tattooed on her thigh (however PLEASE NOTE: the artwork I'm providing here is very similar but is not the final artwork -- it will be replaced). I've attached the text, which includes a line from a poem that she wrote about the tattoo. You are welcome to rearrange this text if you have a vision that makes more sense. I will most likely work with the winning designer on a second project in a month or so, to create the event program.

```html
<!DOCTYPE html>
<html lang="en">
<head>
<meta charset="utf-8">
<title>Marlene's 75th Birthday Invitation</title>
<link href="https://fonts.googleapis.com/css2?family=Arvo&family=Dancing+Script:wght@500;700&family=Nunito+Sans:wght@700&display=swap" rel="stylesheet">
<style>
  :root {
    --backdrop: #c8141c;
    --deep-sea: #101c6a;
    --sea-mid: #1d3d9e;
    --sea-light: #4f92e2;
    --magenta: #d81b7a;
    --blush: #f9dbe9;
    --blush-pale: #fbe6ef;
    --petal: #f3a6c6;
    --ink: #1a1a1a;
    --white: #ffffff;
  }
  * { margin: 0; padding: 0; box-sizing: border-box; }
  html, body { width: 869px; height: 1200px; overflow: hidden; }
  body { background: var(--backdrop); position: relative; }

  .invitation {
    position: absolute; left: 126px; top: 28px;
    width: 631px; height: 975px;
    background: linear-gradient(180deg, var(--blush) 0%, var(--blush-pale) 60%, var(--blush) 100%);
    overflow: hidden;
    font-family: "Arvo", serif;
    color: var(--ink);
  }

  .sea-header { position: absolute; left: 0; top: 0; width: 631px; height: 360px; }
  .sea-header svg { display: block; }

  .salmon-art {
    position: absolute; left: 364px; top: 22px; width: 232px; height: 292px;
    border-radius: 45% 55% 45% 50%;
    background: radial-gradient(ellipse at 50% 45%, rgba(150,170,230,0.45), rgba(110,130,210,0.12) 65%, transparent 72%);
  }

  .poem {
    position: absolute; left: 10px; width: 476px; top: 123px;
    text-align: center;
    font-family: "Dancing Script", cursive;
    font-weight: 500;
    font-size: 22.5px;
    line-height: 34px;
    color: var(--white);
  }
  .poem-credit {
    display: block; font-style: normal; font-weight: 700; color: var(--magenta); font-size: 22.5px;
  }

  .details {
    position: absolute; left: 0; width: 631px; top: 372px;
    text-align: center; font-size: 18px; line-height: 28px;
  }
  .highlight {
    font-family: "Nunito Sans", sans-serif; font-weight: 700; color: var(--magenta); font-size: 18px;
  }
  .event-when { margin-top: 26px; }
  .event-when p { font-family: "Nunito Sans", sans-serif; font-weight: 700; color: var(--magenta); font-size: 18px; }
  .programme { margin-top: 12px; }
  .gift-note { margin-top: 12px; }

  .petal-field {
    position: absolute; left: 0; bottom: 0; width: 631px; height: 300px;
    background:
      radial-gradient(ellipse at 20% 85%, var(--petal) 0%, transparent 45%),
      radial-gradient(ellipse at 75% 80%, var(--petal) 0%, transparent 50%),
      radial-gradient(ellipse at 90% 25%, rgba(243,166,198,0.7) 0%, transparent 30%),
      radial-gradient(ellipse at 10% 20%, rgba(243,166,198,0.5) 0%, transparent 25%),
      linear-gradient(180deg, transparent 0%, rgba(243,166,198,0.45) 55%, var(--petal) 100%);
  }
</style>
</head>
<body>
  <main class="invitation">
    <div class="petal-field" role="img" aria-label="Scattered pink rose petals gathering at the bottom of the card"></div>

    <header class="sea-header">
      <svg width="631" height="360" viewBox="0 0 631 360" role="img" aria-label="Deep blue underwater scene with sunlight rays and bubbles">
        <defs>
          <radialGradient id="seaGlow" cx="0.42" cy="0" r="0.9">
            <stop offset="0" stop-color="#4f92e2"/>
            <stop offset="0.45" stop-color="#1d3d9e"/>
            <stop offset="1" stop-color="#101c6a"/>
          </radialGradient>
        </defs>
        <path d="M0 0 H631 V330 C520 344 430 352 340 348 C220 343 100 322 0 314 Z" fill="url(#seaGlow)"/>
        <path d="M0 314 C100 322 220 343 340 348 C430 352 520 344 631 330 V341 C520 355 430 363 340 359 C220 354 100 333 0 327 Z" fill="#d81b7a"/>
      </svg>
      <div class="salmon-art" role="img" aria-label="Salmon tattoo artwork leaping upward"></div>
    </header>

    <blockquote class="poem">
      What a quiet wonder, the many rivers that run as one<br>
      Old family stories, patient waters and the silver<br>
      Leap of gladness that rises when a child glimpses<br>
      Salmon so close on their steady journey back home.
      <cite class="poem-credit">- Marlene Ashby, River Song</cite>
    </blockquote>

    <section class="details">
      <p>You are warmly invited</p>
      <p>To an intimate family gathering</p>
      <p>In <span class="highlight">Celebration of Marlene’s 75th Birthday</span></p>

      <div class="event-when">
        <p>Sunday, February 15, 2015</p>
        <p>5 to 9 pm</p>
        <p>Riverbend Lodge</p>
        <p>418 N.E. Alder Rd., Cedar Falls, Oregon</p>
      </div>

      <div class="programme">
        <p>Please join us for a light-hearted</p>
        <p>evening of limericks and laughter</p>
        <p>Readings by Marlene from the Riverbenders</p>
        <p>Music by Daniel Crane</p>
        <p>Dinner will be served</p>
      </div>

      <div class="gift-note">
        <p>No gifts, please</p>
        <p>But all are invited to bring something that sheds light --</p>
        <p>candles in glass, penlights, miners lamps</p>
        <p>How has it illuminated your path forward,</p>
        <p>Or guided you in coming home?</p>
      </div>
    </section>
  </main>
</body>
</html>
```